TW Groundworks Capability Statement

I need to design a two page Capability statement for our Civil Construction company that looks professional and can be issued to clients in electronic or print form to show our capabilities.

We have an existing Logo and website https://twgroundworks.com.au/

It should include space for the below:
- Company heading/logo plus ABN, ACN and full contact details
- About Us – Mission, vision, values
- Our Service Offering / Core competencies
- Accreditations/certifications

Designs look the same

```html
<!DOCTYPE html>
<html lang="en">
<head>
<meta charset="utf-8">
<title>TW Groundworks – Capability Statement</title>
<link rel="stylesheet" href="https://fonts.googleapis.com/css2?family=Raleway:wght@400;600;700;800&family=Open+Sans:wght@400;600&display=swap">
<style>
:root{
  --navy:#2b2a80;
  --navy-photo:#4a4a8c;
  --orange:#f7a81b;
  --ink:#3a3a3a;
  --paper:#ffffff;
  --backdrop:#e4e4e7;
  --band:#e6e6e6;
}
*{margin:0;padding:0;box-sizing:border-box}
html,body{width:901px;height:1200px;overflow:hidden;background:var(--backdrop)}
body{position:relative;font-family:"Open Sans",Arial,sans-serif;color:var(--ink)}
.page{position:absolute;top:292px;width:570px;height:806px;background:var(--paper);transform:scale(.754);transform-origin:0 0;box-shadow:0 2px 6px rgba(0,0,0,.12);overflow:hidden}
.page--front{left:12px}
.page--services{left:459px}
.abs{position:absolute}
.heading{font-family:"Raleway",Arial,sans-serif;font-weight:700;text-transform:uppercase;letter-spacing:.2px}
.heading--navy{color:var(--navy);font-size:16px}
.heading--orange{color:var(--orange);font-size:14px}
.body-text{font-size:8.6px;line-height:1.52;text-align:justify}
.hero-art{position:absolute;left:0;top:0}
.brand{position:absolute;display:flex;align-items:center;gap:7px}
.brand__square{width:26px;height:26px;background:var(--navy)}
.brand__name{font-family:"Raleway",Arial,sans-serif;font-weight:800;font-size:19px;color:var(--navy);line-height:1}
.tagline{right:43px;top:114px;width:226px;text-align:right;font-family:"Raleway",Arial,sans-serif;font-size:15.5px;line-height:1.2;color:#333}
.title{left:30px;top:272px;font-family:"Raleway",Arial,sans-serif;font-weight:800;font-size:37px;line-height:.98;color:#fff}
.bullets{display:grid;grid-template-columns:1fr 1fr;column-gap:10px;row-gap:4px;list-style:none;font-size:7.6px;line-height:1.25}
.bullets li{position:relative;padding-left:11px}
.bullets li::before{content:"";position:absolute;left:0;top:1.5px;width:6px;height:6px;border-radius:50%;background:var(--navy)}
.contact__head{font-family:"Raleway",Arial,sans-serif;font-weight:700;font-size:12.5px;color:var(--navy)}
.contact__row{display:flex;align-items:center;font-family:"Raleway",Arial,sans-serif;font-size:11.5px;color:#333;height:17px}
.contact__name{width:88px}
.contact__phone{font-weight:700;color:#222}
.icon{width:11px;height:11px;margin-right:7px;flex:none}
.web{font-size:9.5px}
.social{display:flex;gap:6px}
.social span{width:25px;height:25px;border-radius:50%;border:3px solid var(--navy);display:block}
.footer-bar{position:absolute;left:0;bottom:0;width:570px;height:10px}
.cert-band{left:0;top:614px;width:570px;height:92px;background:var(--band)}
.cert-tab{left:200px;top:614px;width:170px;height:24px}
.cert-tab__label{left:200px;top:618px;width:170px;text-align:center;font-family:"Raleway",Arial,sans-serif;font-weight:700;font-size:13px;color:#fff}
</style>
</head>
<body>

<!-- Front page -->
<section class="page page--front">
  <svg class="hero-art" width="570" height="345" viewBox="0 0 570 345">
    <defs>
      <linearGradient id="heroTone" x1="0" y1="0" x2="1" y2="1">
        <stop offset="0" stop-color="#5e6aa6"/>
        <stop offset=".6" stop-color="#4a4a8c"/>
        <stop offset="1" stop-color="#2f2d7e"/>
      </linearGradient>
    </defs>
    <polygon points="90,17 553,17 553,340 545,340 545,25 90,25" fill="var(--orange)"/>
    <polygon points="18,17 90,17 545,340 18,340" fill="url(#heroTone)" role="img" aria-label="Photo of an excavator digging earth on a civil works site, tinted purple"/>
  </svg>
  <div class="brand" style="left:388px;top:50px">
    <span class="brand__square"></span><span class="brand__name">TW<br><span style="font-size:9px">GROUNDWORKS</span></span>
  </div>
  <p class="abs tagline">Tier 1 engineering &amp; project management capability with nimble privately owned and operated mentality.</p>
  <h1 class="abs title">CAPABILITY<br>STATEMENT</h1>

  <h2 class="abs heading heading--navy" style="left:30px;top:372px">About TW Groundworks</h2>
  <p class="abs body-text" style="left:30px;top:398px;width:514px">TW Groundworks is a specialist utilities contractor leveraging industry experience to provide exceptional outcomes. We are a client focused business that takes a ‘best-for-project’ approach in everything we do, and see honest, timely and transparent communication as one of our key strengths. Our business works in complex, high-risk environments and understands all safety, quality, and environmental considerations. We meticulously plan our projects with these key factors in mind, ensuring the requirements of the specific tasks are understood and well documented to satisfy our robust internal processes and rigorous external auditing.</p>

  <h3 class="abs heading heading--orange" style="left:30px;top:500px">Mission</h3>
  <p class="abs body-text" style="left:30px;top:524px;width:248px">Lorem Ipsum is simply dummy text of the printing and typesetting industry. Lorem Ipsum has been the industry's standard dummy text ever since the 1500s, when an unknown printer took a galley of type and scrambled it to make a type specimen book. It has survived not only five centuries, but also the leap into electronic typesetting, remaining essentially unchanged.</p>
  <p class="abs body-text" style="left:30px;top:630px;width:248px">Lorem Ipsum is simply dummy text of the printing and typesetting industry. Lorem Ipsum has been the industry's standard dummy text ever since the 1500s, when an unknown printer took a galley of type</p>

  <h3 class="abs heading heading--orange" style="left:295px;top:500px">Vision</h3>
  <p class="abs body-text" style="left:295px;top:524px;width:249px">Lorem Ipsum is simply dummy text of the printing and typesetting industry. Lorem Ipsum has been the industry's standard dummy text ever since the 1500s, when an unknown printer.</p>
  <h3 class="abs heading heading--orange" style="left:295px;top:605px">Values</h3>
  <p class="abs body-text" style="left:295px;top:630px;width:249px">Lorem Ipsum is simply dummy text of the printing and typesetting industry. Lorem Ipsum has been the industry's standard dummy text ever since the 1500s, when an unknown printer.</p>

  <p class="abs contact__head" style="left:28px;top:730px">CONTACT US TODAY</p>
  <div class="abs" style="left:28px;top:752px">
    <div class="contact__row"><span class="contact__name">Daniel Hartley</span><svg class="icon" viewBox="0 0 12 12"><circle cx="6" cy="6" r="6" fill="var(--orange)"/><path d="M4 3.2l1 1.6-.6.7a4 4 0 0 0 2.1 2.1l.7-.6 1.6 1-.5 1A5.5 5.5 0 0 1 3 4z" fill="#fff"/></svg><span class="contact__phone">0400 118 240</span></div>
    <div class="contact__row"><span class="contact__name">Marcus Wyatt</span><svg class="icon" viewBox="0 0 12 12"><circle cx="6" cy="6" r="6" fill="var(--orange)"/><path d="M4 3.2l1 1.6-.6.7a4 4 0 0 0 2.1 2.1l.7-.6 1.6 1-.5 1A5.5 5.5 0 0 1 3 4z" fill="#fff"/></svg><span class="contact__phone">0400 552 917</span></div>
  </div>
  <div class="abs" style="left:238px;top:750px">
    <div class="contact__row web"><svg class="icon" viewBox="0 0 12 12"><circle cx="6" cy="6" r="6" fill="var(--orange)"/><rect x="3" y="4" width="6" height="4" fill="none" stroke="#fff"/></svg>tenders@twgroundworks.com.au</div>
    <div class="contact__row web"><svg class="icon" viewBox="0 0 12 12"><circle cx="6" cy="6" r="6" fill="var(--orange)"/><circle cx="6" cy="6" r="3" fill="none" stroke="#fff"/></svg>www.twgroundworks.com.au</div>
  </div>
  <p class="abs heading heading--orange" style="left:447px;top:730px;font-size:12.5px">Follow us</p>
  <div class="abs social" style="left:447px;top:754px"><span></span><span></span><span></span></div>

  <svg class="footer-bar" viewBox="0 0 570 10" preserveAspectRatio="none">
    <rect width="570" height="10" fill="var(--navy)"/>
    <polygon points="445,0 570,0 570,10 455,10" fill="var(--orange)"/>
  </svg>
</section>

<!-- Services page -->
<section class="page page--services">
  <svg class="hero-art" width="570" height="260" viewBox="0 0 570 260">
    <defs>
      <linearGradient id="svcTone" x1="0" y1="0" x2="1" y2="1">
        <stop offset="0" stop-color="#f7b431"/>
        <stop offset="1" stop-color="#e7a21e"/>
      </linearGradient>
    </defs>
    <g role="img" aria-label="Photo of site workers surveying with a drone, tinted navy and orange">
      <rect x="28" y="25" width="222" height="222" fill="url(#svcTone)"/>
      <polygon points="28,25 250,247 28,247" fill="var(--navy-photo)"/>
    </g>
  </svg>

  <h2 class="abs heading heading--navy" style="left:262px;top:26px">Our Services</h2>
  <p class="abs body-text" style="left:262px;top:52px;width:286px">TW Groundworks prides itself on being a customer focused business, that takes the time to understand our clients’ key drivers and ensure we work collaboratively to achieve positive outcomes. We have a team of highly experienced project management professionals who are genuine, responsive, and transparent which enables us to make our client lives easier from the design phase to project completion. We have a self-perform field resource that carries enviable experience, which is supplemented by hand-picked sub-contractors that are known in the industry and are trusted partners. We understand that quality and safety are paramount in every aspect of our work. We prioritise the use of superior materials, employ skilled professionals,</p>
  <p class="abs" style="left:264px;top:237px;font-size:8.6px">Below are TW Groundworks key offerings:</p>

  <h3 class="abs heading heading--orange" style="left:28px;top:272px;font-size:13px">Project / Program Management</h3>
  <p class="abs body-text" style="left:28px;top:298px;width:251px">As a business we are focused on delivering for our clients from a projects inception to its completion. Our team have a deep understanding of engineering and construction principles and couples this with exceptional communication and reporting which is the core of our service offering. We are a passionate group who are constantly striving to exceed best practice and find innovative ways to solve the inevitable challenges faced in construction.</p>

  <h3 class="abs heading heading--orange" style="left:297px;top:272px;font-size:13px">Water Infrastructure</h3>
  <p class="abs body-text" style="left:297px;top:298px;width:250px">Water infrastructure plays a crucial role in society, ensuring the reliable supply of clean and safe water to communities. It encompasses a vast network of pipework and facilities that enable us to meet our basic human needs, such as drinking, cooking, and sanitation.</p>
  <ul class="abs bullets" style="left:297px;top:380px;width:255px">
    <li>Complex live connections</li><li>Domestic water services</li>
    <li>Meter assemblies</li><li>Butt welding of PE pipelines</li>
    <li>Reticulation mains and larger pipelines</li><li>Relocation of existing water assets</li>
  </ul>

  <h3 class="abs heading heading--orange" style="left:28px;top:456px;font-size:13px">Gas Infrastructure</h3>
  <p class="abs body-text" style="left:28px;top:482px;width:251px">TW Groundworks has a wide-ranging capability in the gas infrastructure space with a knowledgeable team that is highly trained and acutely aware of the required processes and procedures to follow when installing such assets.</p>
  <ul class="abs bullets" style="left:28px;top:562px;width:251px;grid-template-columns:1.25fr 1fr">
    <li>Butt welding and electro-fusion</li><li>Pressure testing</li>
    <li>Pre-laid gas services</li><li>Complex gas tie-ins</li>
  </ul>

  <h3 class="abs heading heading--orange" style="left:297px;top:456px;font-size:13px">Civil Construction</h3>
  <p class="abs body-text" style="left:297px;top:482px;width:250px">Outside the Utilities space we can assist with an array of civil construction works and have proven capabilities in the below areas.</p>
  <ul class="abs bullets" style="left:297px;top:544px;width:255px;grid-template-columns:1.6fr 1fr">
    <li>Bulk earthworks</li><li>Landscaping</li>
    <li>Rehabilitation works</li><li>General Civil works</li>
    <li>Detailed excavations</li>
  </ul>

  <div class="abs cert-band"></div>
  <svg class="abs cert-tab" viewBox="0 0 170 24"><polygon points="0,0 170,0 160,24 10,24" fill="var(--navy)"/></svg>
  <p class="abs cert-tab__label">CERTIFICATIONS</p>

  <p class="abs contact__head" style="left:28px;top:730px">CONTACT US TODAY</p>
  <div class="abs" style="left:28px;top:752px">
    <div class="contact__row"><span class="contact__name">Daniel Hartley</span><svg class="icon" viewBox="0 0 12 12"><circle cx="6" cy="6" r="6" fill="var(--orange)"/><path d="M4 3.2l1 1.6-.6.7a4 4 0 0 0 2.1 2.1l.7-.6 1.6 1-.5 1A5.5 5.5 0 0 1 3 4z" fill="#fff"/></svg><span class="contact__phone">0400 118 240</span></div>
    <div class="contact__row"><span class="contact__name">Marcus Wyatt</span><svg class="icon" viewBox="0 0 12 12"><circle cx="6" cy="6" r="6" fill="var(--orange)"/><path d="M4 3.2l1 1.6-.6.7a4 4 0 0 0 2.1 2.1l.7-.6 1.6 1-.5 1A5.5 5.5 0 0 1 3 4z" fill="#fff"/></svg><span class="contact__phone">0400 552 917</span></div>
  </div>
  <div class="abs" style="left:238px;top:750px">
    <div class="contact__row web"><svg class="icon" viewBox="0 0 12 12"><circle cx="6" cy="6" r="6" fill="var(--orange)"/><rect x="3" y="4" width="6" height="4" fill="none" stroke="#fff"/></svg>tenders@twgroundworks.com.au</div>
    <div class="contact__row web"><svg class="icon" viewBox="0 0 12 12"><circle cx="6" cy="6" r="6" fill="var(--orange)"/><circle cx="6" cy="6" r="3" fill="none" stroke="#fff"/></svg>www.twgroundworks.com.au</div>
  </div>
  <div class="abs" style="left:438px;top:752px;display:flex;gap:6px;font-family:'Raleway',Arial,sans-serif;font-size:9.5px;line-height:1.15;color:#333">
    <svg class="icon" style="margin:0" viewBox="0 0 12 12"><circle cx="6" cy="6" r="6" fill="var(--orange)"/><path d="M6 2.5a2.2 2.2 0 0 1 2.2 2.2C8.2 6.3 6 9 6 9S3.8 6.3 3.8 4.7A2.2 2.2 0 0 1 6 2.5z" fill="#fff"/></svg>
    <span>7/18 Ironbark Way,<br>Westfield<br>VIC 3000</span>
  </div>

  <svg class="footer-bar" viewBox="0 0 570 10" preserveAspectRatio="none">
    <rect width="570" height="10" fill="var(--navy)"/>
    <polygon points="445,0 570,0 570,10 455,10" fill="var(--orange)"/>
  </svg>
</section>

</body>
</html>
```